Modern and appealing business Wordpress site

I've been operating my consulting firm for 5 years and feel like it is time to really improve on my web presence as I'm starting to get more national attention. I had a logo made through this service a couple of years ago, and would like to get a website that matches the look of it. The website will be used to (1) advertise my services (2) provide a brief overview of our management philosophies, and (3) host a resource library database. I understand HTML, but am not as familiar with how to code Wordpress, so I need someone that can help upload themes.

The website can be found at www.trelmondgroup.com.

For design, I prefer round designs to square and want the color scheme to match the attached logo. I have included both the full logo and the abbreviated one.

I also have a new picture for CFO uploaded. I plan on getting a new one for the CEO in the coming weeks, so I would like someone that I could get to help make the modification at a later time.

The resource database will be put into a document library (probably Kiln7) once the final design is completed rather than having multiple pages with links...just so you know the final vision for the site.

Reach out if you have any questions.

Target Market(s)

Community Action Agencies, Nonprofit Organization Leaders

Industry/Entity Type

Consulting

Coding

Coded - Design and coding required

Font styles to use
Sans Serif

Requirements
Must have
• Must match the color scheme of the attached logo

```html
<!DOCTYPE html>
<html lang="en">
<head>
<meta charset="utf-8">
<title>Trelmond Group – Consulting</title>
<link rel="stylesheet" href="https://fonts.googleapis.com/css2?family=Montserrat:wght@500;600;700&family=Open+Sans:wght@400;600&display=swap">
<style>
:root{
  --blue:#2f9fd6;
  --blue-dark:#0e4a62;
  --ink:#1d1d1d;
  --text:#5c5c5c;
  --muted:#8a8a8a;
  --rule:#555;
  --gray-bg:#efefef;
  --white:#fff;
  --gold:#f3d23a;
}
*{box-sizing:border-box;margin:0;padding:0}
html,body{width:1200px;height:3127px;overflow:hidden}
body{font-family:"Open Sans",Arial,sans-serif;color:var(--text);background:var(--white);position:relative}
.wrap{position:absolute;left:113px;width:974px}
h1,h2,h3,h4,.nav a,.brand{font-family:"Montserrat",Arial,sans-serif}

.topbar{position:absolute;top:0;left:0;width:1200px;height:44px;background:var(--blue);color:#fff;font-size:11px;display:flex;justify-content:flex-end;align-items:center;gap:28px;padding-right:113px}
.topbar span{display:flex;align-items:center;gap:10px}

.header{position:absolute;top:44px;left:0;width:1200px;height:69px;background:#f7f7f7;border-bottom:1px solid #e3e3e3}
.brand{position:absolute;left:113px;top:20px;display:flex;align-items:center;gap:8px;font-weight:700;font-size:22px;color:var(--blue);letter-spacing:1px}
.brand i{display:block;width:28px;height:28px;border-radius:50%;background:var(--blue)}
.nav{position:absolute;left:495px;top:25px;display:flex;gap:27px}
.nav a{font-size:14px;font-weight:500;color:var(--ink);text-decoration:none}
.nav a.active{color:var(--blue)}
.social-top{position:absolute;left:1013px;top:28px;display:flex;gap:17px}
.social-top i{display:block;width:12px;height:12px;border-radius:50%;background:var(--blue)}

.hero{position:absolute;top:113px;left:0;width:1200px;height:414px;background:radial-gradient(ellipse at 62% 45%,#c9a06a 0%,#d9c3a2 18%,#ece8e2 42%,#f2f2f1 70%),#eee}
.cta-band{position:absolute;top:527px;left:0;width:1200px;height:68px;background:var(--blue);overflow:hidden}
.cta-band h2{position:absolute;left:113px;top:23px;color:#fff;font-size:17px;font-weight:700}
.btn-quote{position:absolute;left:957px;top:15px;width:130px;height:39px;background:var(--blue-dark);color:#fff;font:700 12px "Montserrat",sans-serif;display:flex;align-items:center;justify-content:center;gap:10px;border-radius:2px}

.section-title{font-weight:700;color:var(--blue)}
.bar{display:block;width:30px;height:4px;background:var(--rule);border-radius:2px}

.overview-text{top:655px;width:476px}
.overview-text h2{font-size:32px;margin-bottom:12px}
.overview-text p{font-size:12.5px;line-height:23px;margin-top:22px}
.mission{margin-top:36px;background:#f0f0f0;border-left:4px solid var(--gold);padding:19px 26px 18px 27px;font-size:12.5px;line-height:23px}
.overview-photo{position:absolute;left:613px;top:647px;width:474px;height:316px;background:linear-gradient(135deg,#3a4450 0%,#7b8790 40%,#c9ced2 70%,#8a98a6 100%)}

.cards{top:1030px;display:flex;gap:27px}
.card{position:relative;width:307px;height:281px;overflow:hidden}
.card .photo{position:absolute;inset:0}
.card .label{position:absolute;left:0;bottom:0;width:100%;height:62px;background:rgba(70,70,70,.82);display:flex;align-items:center;gap:12px;padding-left:26px;color:#fff;font:700 14px "Montserrat",sans-serif}
.card.text{background:linear-gradient(180deg,#7a7a7a,#8d8d8d);padding:22px 26px;color:#fff}
.card.text h4{font-size:14px;display:flex;align-items:center;gap:10px;margin-bottom:14px}
.card.text p{font-size:11px;line-height:21px}

.resources{position:absolute;top:1370px;left:0;width:1200px;height:594px;background:var(--gray-bg)}
.resources h2{position:absolute;top:56px;width:100%;text-align:center;font-size:40px}
.resources .bar{position:absolute;top:116px;left:585px}
.res-grid{position:absolute;top:146px;left:113px;width:1000px}
.res{position:absolute;width:307px;padding:28px 6px 0 87px}
.res.hi{background:#fff;height:157px;box-shadow:0 0 4px rgba(0,0,0,.05)}
.res svg{position:absolute;left:17px;top:32px}
.res h3{font-size:15px;font-weight:600;color:var(--ink);line-height:19px;margin-bottom:7px;white-space:nowrap}
.res h3.wrap2{white-space:normal}
.res p{font-size:11px;line-height:16px;color:var(--muted);padding-right:14px}

.excellence{position:absolute;top:1964px;left:8px;width:1184px;height:203px;background:linear-gradient(100deg,#79c4e8 0%,#48ade0 40%,#2d8fc5 75%,#2a82b8 100%)}
.excellence h2{position:absolute;top:68px;width:100%;text-align:center;font-size:35px;font-weight:700;color:#111}
.excellence h2 span{color:#fff}
.excellence .bar{position:absolute;top:120px;left:577px}

.testimonials h2{position:absolute;top:2250px;width:1200px;text-align:center;font-size:40px}
.testimonials .bar{position:absolute;top:2310px;left:585px}
.quote{position:absolute;top:2381px;width:486px;display:flex;gap:26px}
.quote .portrait{flex:0 0 224px;height:223px}
.quote h3{font-size:17px;color:var(--blue);line-height:19px;margin-bottom:9px}
.quote p{font-size:12.5px;line-height:19.5px;color:#444}

.footer{position:absolute;top:2721px;left:0;width:1200px;height:406px;background:var(--blue);color:#fff}
.fcol{position:absolute;top:84px;width:307px}
.fcol h3{font-size:22px;font-weight:700;padding-bottom:15px;border-bottom:1px solid rgba(255,255,255,.35)}
.fcol p{margin-top:30px;font-size:11px;line-height:19.5px;color:#cde8f6}
.links{margin-top:28px;display:grid;grid-template-columns:171px 130px;row-gap:15px;font-size:11.5px}
.subscribe{margin-top:8px;display:flex;height:33px}
.subscribe span{flex:1;background:#fff;color:#999;font-size:11px;padding:10px 14px}
.subscribe b{width:36px;background:var(--blue-dark);display:flex;align-items:center;justify-content:center}
.fnote{font-size:11px;margin-top:14px;color:#d8eef9}
.fbottom{position:absolute;top:349px;left:113px;width:974px;border-top:1px solid rgba(255,255,255,.35);padding-top:16px;font-size:11px}
.fsocial{position:absolute;right:0;top:10px;display:flex;gap:8px}
.fsocial i{display:block;width:28px;height:28px;border-radius:50%;background:#fff}
</style>
</head>
<body>

<div class="topbar">
  <span><svg width="12" height="14" viewBox="0 0 12 14"><path d="M6 1a4.5 4.5 0 0 0-4.5 4.5C1.5 9 6 13 6 13s4.5-4 4.5-7.5A4.5 4.5 0 0 0 6 1z" fill="none" stroke="#fff" stroke-width="1.4"/><circle cx="6" cy="5.5" r="1.6" fill="#fff"/></svg>48 Harlow Street, NY 10027 US.</span>
  <span><svg width="14" height="14" viewBox="0 0 14 14"><circle cx="7" cy="7" r="5.8" fill="none" stroke="#fff" stroke-width="1.4"/><path d="M7 3.8V7l2.2 1.4" stroke="#fff" stroke-width="1.4" fill="none"/></svg>Mon - Sat 8.00 - 18.00. Sunday CLOSED</span>
  <span><svg width="14" height="14" viewBox="0 0 14 14"><path d="M3 1l2.4 2.6-1.2 1.8a8 8 0 0 0 4.4 4.4l1.8-1.2L13 11l-1.6 2C6 13 1 8 1 2.6z" fill="#fff"/></svg>212 555 0148</span>
</div>

<header class="header">
  <div class="brand"><i></i>TRELMOND</div>
  <nav class="nav">
    <a class="active">Home</a><a>Services</a><a>Roma</a><a>Madd</a><a>Resource</a><a>Contacts</a>
  </nav>
  <div class="social-top"><i></i><i></i><i></i></div>
</header>

<div class="hero" role="img" aria-label="Close-up of a wooden chess pawn in front of a row of blurred light pawns on a chessboard"></div>

<div class="cta-band">
  <h2>Looking For A First-Class Business Consultant?</h2>
  <div class="btn-quote">Get a quote <svg width="7" height="10" viewBox="0 0 7 10"><path d="M1 1l4 4-4 4" stroke="#fff" stroke-width="2" fill="none"/></svg></div>
</div>

<section class="wrap overview-text">
  <h2 class="section-title">company overview</h2>
  <span class="bar"></span>
  <p>Trelmond Group was created to help nonprofits and government contractors meet their basic funding requirements and adopt a Mission Aligned Data Driven mindset that promotes positive change in the lives of the people they serve. Our approach is not simply based off of theoretical business practices, but on practical solutions to real-life situations learned through more than twenty years of experience.</p>
  <div class="mission">To help social service organizations develop a Mission Aligned Data Driven mindset that promotes positive change in the lives of the customers they serve.</div>
</section>
<div class="overview-photo" role="img" aria-label="Three colleagues reviewing charts on a tablet at a meeting table"></div>

<section class="wrap cards">
  <div class="card">
    <div class="photo" role="img" aria-label="Hands holding a pen over printed bar and line charts" style="background:linear-gradient(135deg,#5a4a45 0%,#d8dde3 35%,#eef0f3 55%,#6e9fd6 80%,#c9a98f 100%)"></div>
    <div class="label"><svg width="34" height="30" viewBox="0 0 34 30"><rect x="2" y="2" width="30" height="19" fill="none" stroke="#2f9fd6" stroke-width="2"/><path d="M7 16l6-6 5 4 8-7" stroke="#2f9fd6" stroke-width="2" fill="none"/><path d="M11 21l-4 8M23 21l4 8M17 21v6" stroke="#2f9fd6" stroke-width="2"/></svg>Training &amp; Consulting</div>
  </div>
  <div class="card text">
    <h4><svg width="34" height="34" viewBox="0 0 34 34"><circle cx="17" cy="17" r="14" fill="none" stroke="#2f9fd6" stroke-width="4" stroke-dasharray="6 2"/></svg>Data Analytics</h4>
    <p>One the most important, and frequently neglected, areas of organizational management is the analysis of data to accurately identify community needs and track progress towards the successful fulfillment of the entity's purpose. Our goal is to ensure each of our customers is equipped with the tools necessary to obtain objective data that will allow for quality decision making.</p>
  </div>
  <div class="card">
    <div class="photo" role="img" aria-label="Businessman in a white shirt and tie working at a desk in a bright office" style="background:linear-gradient(135deg,#f3f3f3 0%,#d8d4cf 40%,#8d8a88 70%,#e7e7e7 100%)"></div>
    <div class="label"><svg width="36" height="36" viewBox="0 0 36 36"><circle cx="18" cy="18" r="15" fill="#2f9fd6"/><path d="M9 14c5-2 8 2 12 0M12 25c4-3 8-1 12-4" stroke="#fff" stroke-width="2" fill="none"/></svg>Storytelling</div>
  </div>
</section>

<section class="resources">
  <h2 class="section-title">Resources</h2>
  <span class="bar"></span>
  <div class="res-grid">
    <div class="res" style="left:0;top:0">
      <svg width="58" height="52" viewBox="0 0 58 52"><path d="M15 2h28l14 24-14 24H15L1 26z" fill="none" stroke="#2f9fd6" stroke-width="2.5"/><path d="M18 27l20-6-3 4 5 1-2 2-6-1-6 5-2-1 3-4z" fill="#2f9fd6"/></svg>
      <h3>Board Governance</h3><p>Company that offers design and build services for you from initial sketches to the final production.</p>
    </div>
    <div class="res hi" style="left:334px;top:0">
      <svg width="58" height="52" viewBox="0 0 58 52"><path d="M15 2h28l14 24-14 24H15L1 26z" fill="none" stroke="#2f9fd6" stroke-width="2.5"/><path d="M20 17v17h18M23 30l5-6 4 3 5-7" stroke="#2f9fd6" stroke-width="2" fill="none"/></svg>
      <h3>Organizational Leadership</h3><p>We consider all the drivers of change – from the ground up and we'll motivate and support you to make the change.</p>
    </div>
    <div class="res" style="left:668px;top:0">
      <svg width="58" height="52" viewBox="0 0 58 52"><path d="M15 2h28l14 24-14 24H15L1 26z" fill="none" stroke="#2f9fd6" stroke-width="2.5"/><path d="M17 18h4l3 11h12l3-8H22" stroke="#2f9fd6" stroke-width="2.5" fill="none"/><circle cx="26" cy="33" r="2" fill="#2f9fd6"/><circle cx="34" cy="33" r="2" fill="#2f9fd6"/></svg>
      <h3>Needs Assessments</h3><p>Design repeatable growth models and innovation pipelines that generate new products with higher potential and lower risks of failure.</p>
    </div>
    <div class="res" style="left:0;top:184px">
      <svg width="58" height="52" viewBox="0 0 58 52"><path d="M15 2h28l14 24-14 24H15L1 26z" fill="none" stroke="#2f9fd6" stroke-width="2.5"/><path d="M18 21l11-6 11 6zM20 23v9M25 23v9M33 23v9M38 23v9M17 34h24" stroke="#2f9fd6" stroke-width="2.5" fill="#2f9fd6"/></svg>
      <h3>Strategic Planning</h3><p>We work buy-side and sell-side and give our clients hard-hitting and objective answers and focus hard on the best opportunities.</p>
    </div>
    <div class="res" style="left:334px;top:184px">
      <svg width="58" height="52" viewBox="0 0 58 52"><path d="M15 2h28l14 24-14 24H15L1 26z" fill="none" stroke="#2f9fd6" stroke-width="2.5"/><path d="M24 15h10l-2 13h-6zM25 31h8M26 35h6" stroke="#2f9fd6" stroke-width="2.5" fill="#2f9fd6"/></svg>
      <h3>Succession Planning</h3><p>We work across all the major geographies, meaning we understand the underlying drivers in construction markets.</p>
    </div>
    <div class="res" style="left:668px;top:184px">
      <svg width="58" height="52" viewBox="0 0 58 52"><path d="M15 2h28l14 24-14 24H15L1 26z" fill="none" stroke="#2f9fd6" stroke-width="2.5"/><path d="M16 19h16v11H16zM32 23h6l3 4v3h-9z" fill="#2f9fd6"/><circle cx="21" cy="32" r="2.5" fill="#2f9fd6"/><circle cx="36" cy="32" r="2.5" fill="#2f9fd6"/></svg>
      <h3 class="wrap2">Policies and Procedures Guides</h3><p>Scheduled transport operations, from broad market trends and strategy to the development of integrated commercial strategies.</p>
    </div>
  </div>
</section>

<section class="excellence" role="img" aria-label="Blue-tinted photo of hands working on business documents">
  <h2>Leading Organizations <span>to Excellence !</span></h2>
  <span class="bar"></span>
</section>

<section class="testimonials">
  <h2 class="section-title">Testimonials</h2>
  <span class="bar"></span>
  <div class="quote" style="left:113px">
    <div class="portrait" role="img" aria-label="Portrait of a smiling woman with glasses in a bright office" style="background:linear-gradient(135deg,#d7dbe0 0%,#b08a6a 45%,#9fb3cf 75%,#e6e6e6 100%)"></div>
    <div><h3>Maple County Senior Services</h3><p>It was a training, but not your typical training. It leaves you with a new and different take on things. You will find yourself saying 'Wow, I've never thought of it like that before'. You will be left with new and refreshing ideas and different ways to approach situations</p></div>
  </div>
  <div class="quote" style="left:618px">
    <div class="portrait" role="img" aria-label="Portrait of a smiling bearded man in glasses and a tan shirt" style="background:linear-gradient(135deg,#e9e9e9 0%,#cfcfcf 35%,#b8845a 60%,#8a6a55 85%,#dcdcdc 100%)"></div>
    <div><h3>Community Action Partnership of Riverbend</h3><p>Dana is easy to work with and his expertise allows you to tailor your training to the specific needs of your agency. We highly recommend Dana and his company.</p></div>
  </div>
</section>

<footer class="footer">
  <div class="fcol" style="left:113px"><h3>About Us</h3><p>Trelmond Insights - Before we talk destination, we shine a spotlight across your organization to fully understand its people, processes, and technology. Strategy, data and training for mission-driven teams.</p></div>
  <div class="fcol" style="left:447px"><h3>Extra Links</h3>
    <div class="links"><span>About</span><span>News</span><span>Contacts</span><span>Testimonials</span><span>Typography</span><span>Services</span><span>Careers</span><span>Our team</span><span>Shop</span><span>Our approach</span></div>
  </div>
  <div class="fcol" style="left:780px"><h3>subscribe</h3>
    <div class="subscribe"><span>Enter Your E-mail</span><b><svg width="14" height="11" viewBox="0 0 14 11"><rect x="1" y="1" width="12" height="9" fill="none" stroke="#fff" stroke-width="1.5"/><path d="M1 1l6 5 6-5" stroke="#fff" stroke-width="1.5" fill="none"/></svg></b></div>
    <p class="fnote">Get latest updates and offers.</p>
  </div>
  <div class="fbottom">© 2022 Consulting trelmondgroup
    <div class="fsocial"><i></i><i></i></div>
  </div>
</footer>

</body>
</html>
```